Mosque App design fresh look and feel

Need to create a mosque app which has half a couple of dozen pages, a login page will take you into the main information with about 6 categories, such as school, memberships, information, prayer times etc... we have 3 types of users... 1. User .. admin user 3. imam user

I have xd files available.
https://mockview.plorvent.com/view/e81f27da-5c04-4b9e-91a3-7fd20b6c4a85-3c1d/

Target Market(s)

Muslims

Font styles to use
Sans Serif

Requirements
Must have
• Great UI
Simple flow

```html
<!DOCTYPE html>
<html lang="en">
<head>
<meta charset="utf-8">
<title>Noorhall – Mosque App Screens</title>
<link rel="stylesheet" href="https://fonts.googleapis.com/css2?family=Poppins:wght@400;500;600;700&family=Roboto:wght@400;500&display=swap">
<style>
:root{
  --green:#17a061;
  --green-dark:#0f9a57;
  --green-light:#44bf92;
  --ink:#2b2b2b;
  --muted:#8a8a8a;
  --line:#dcdcdc;
  --panel:#eef0f2;
  --canvas:#ffffff;
  --overlay:#9a9a9a;
}
*{box-sizing:border-box;margin:0;padding:0}
html,body{width:1200px;height:3017px;overflow:hidden;background:var(--canvas)}
body{position:relative;font-family:"Roboto",sans-serif;color:var(--ink)}
.screen{position:absolute;width:254px;height:536px;background:#fff;border-radius:14px;overflow:hidden;box-shadow:0 6px 26px rgba(0,0,0,.14)}
.el{position:absolute}
.header{position:absolute;left:0;top:0;width:100%;height:82px;background:linear-gradient(120deg,var(--green-light),var(--green-dark) 70%)}
.header-title{position:absolute;left:0;right:0;top:54px;text-align:center;color:#fff;font-family:"Poppins",sans-serif;font-size:12px}
.back{position:absolute;left:14px;top:55px;width:7px;height:7px;border-left:1.3px solid #fff;border-bottom:1.3px solid #fff;transform:rotate(45deg)}
.brand{position:absolute;left:0;right:0;text-align:center;font-family:"Poppins",sans-serif;font-weight:600;color:var(--green)}
.field{position:absolute;left:14px;width:226px;height:26px;border:1px solid var(--line);font-size:7px;padding:0 8px;display:flex;align-items:center;color:#444}
.field.select::after{content:"";position:absolute;right:9px;top:11px;border:3px solid transparent;border-top:4px solid #333}
.btn{position:absolute;left:14px;width:226px;height:28px;background:linear-gradient(90deg,var(--green-light),var(--green-dark));color:#fff;font-size:9px;display:flex;align-items:center;justify-content:center;border-radius:2px}
.small{font-size:7px;text-align:center;left:0;right:0;color:#333}
.link{color:var(--green)}
.date-bar{position:absolute;left:14px;width:226px;height:28px;background:linear-gradient(90deg,var(--green-light),var(--green-dark));color:#fff;font-size:9px;display:flex;align-items:center;justify-content:center}
.mini-table{position:absolute;left:14px;width:226px;height:30px;border:1px solid var(--line);display:flex}
.mini-table div{flex:1;border-right:1px solid var(--line);font-size:6px;text-align:center;padding-top:5px;line-height:1.5;color:#555}
.mini-table div:last-child{border:none}
.mini-table b{font-weight:500;color:#222}
.radio{position:absolute;top:194px;font-size:8.5px;display:flex;align-items:center;gap:6px}
.radio i{width:10px;height:10px;border:1px solid #bbb;border-radius:50%;display:inline-block}
.radio i.on{border-color:var(--green);box-shadow:inset 0 0 0 2px #fff;background:var(--green)}
.heading{position:absolute;left:14px;font-family:"Poppins",sans-serif;font-size:11px;color:#222}
.amount{position:absolute;top:127px;height:25px;border:1px solid var(--line);font-size:7px;color:var(--muted);display:flex;align-items:center;justify-content:center}
.amount.active{border:1.5px solid var(--green);color:var(--green);font-weight:700;font-size:9px}
.tab{position:absolute;top:309px;height:28px;border:1px solid var(--line);font-size:7px;display:flex;align-items:center;justify-content:center}
.tab.active{border:1.5px solid var(--green);color:var(--green)}
.card-panel{position:absolute;left:13px;top:346px;width:227px;height:86px;background:var(--panel)}
.card-panel span{position:absolute;font-size:6.5px;color:#333}
.card-panel i{position:absolute;height:16px;background:#fff}
.donor{position:absolute;width:229px;height:52px;border:1px solid var(--line);background:#fff}
.avatar{position:absolute;left:16px;top:12px;width:28px;height:28px;border-radius:50%;background:radial-gradient(circle at 50% 40%,#c9b6a5,#6d6258)}
.donor-name{position:absolute;left:56px;top:10px;font-size:7px;font-weight:500;color:#222}
.donor-date{position:absolute;left:56px;top:19px;font-size:5.5px;color:var(--muted)}
.donor-for{position:absolute;left:56px;top:30px;font-size:7px;color:#777}
.pill{position:absolute;right:13px;top:16px;width:53px;height:18px;border-radius:9px;background:linear-gradient(90deg,var(--green-light),var(--green-dark));color:#fff;font-size:9px;font-weight:500;display:flex;align-items:center;justify-content:center}
.month{position:absolute;left:13px;font-family:"Poppins",sans-serif;font-size:11px;color:#222}
.prayer-row{position:absolute;left:12px;width:229px;height:48px;border:1px solid var(--line);font-size:9.5px;color:#222}
.prayer-row span{position:absolute;left:14px;top:17px}
.prayer-row em{position:absolute;right:14px;top:18px;font-style:normal;font-size:9px;color:#444}
.overlay{position:absolute;left:0;top:82px;width:100%;height:454px;background:var(--overlay)}
.behind{position:absolute;left:12px;top:108px;width:229px;height:146px;background:linear-gradient(180deg,#2e7a55,#3f8163);opacity:.8}
.dialog{position:absolute;left:32px;top:108px;width:191px;height:269px;background:#fff}
.dialog-time{height:68px;background:#111;color:#fff;font-family:"Roboto",sans-serif;font-size:40px;font-weight:400;letter-spacing:1px;display:flex;align-items:center;justify-content:center;gap:3px}
.dialog-time small{font-size:10px;align-self:flex-end;margin-bottom:18px}
.done{position:absolute;left:0;bottom:0;width:100%;height:26px;border-top:1px solid var(--line);font-size:8.5px;color:#444;display:flex;align-items:center;justify-content:center}
</style>
</head>
<body>

<!-- Splash -->
<section class="screen splash" style="left:483px;top:183px;height:532px">
  <svg class="el" style="left:85px;top:199px" width="84" height="84" viewBox="0 0 84 84"><circle cx="42" cy="42" r="40" fill="#d6f0e4"/><circle cx="42" cy="42" r="34" fill="#17a061"/></svg>
  <div class="brand" style="top:296px;font-size:17px">Noorhall</div>
</section>

<!-- Log In -->
<section class="screen login" style="left:127px;top:889px">
  <header class="header"><div class="header-title">Log In</div></header>
  <div class="brand" style="top:130px;font-size:20px">Noorhall</div>
  <div class="field" style="top:194px">Email</div>
  <div class="field" style="top:227px">Password</div>
  <div class="btn" style="top:272px">Sign In</div>
  <div class="el small" style="top:316px">ForgotPassword? <span class="link">Click here</span></div>
  <div class="el small" style="top:328px">Dont have account? <span class="link">Create Account</span></div>
  <div class="date-bar" style="top:373px">Friday January 22, 2021</div>
  <div class="mini-table" style="top:401px">
    <div><b>Prayers</b><br>Timing</div><div><b>Fajr</b><br>04:00</div><div><b>Duhr</b><br>01:30</div><div><b>Asar</b><br>04:30</div><div><b>Magrib</b><br>05:45</div><div><b>Isha</b><br>08:45</div>
  </div>
</section>

<!-- Register -->
<section class="screen register" style="left:471px;top:889px">
  <header class="header"><div class="header-title">Register</div></header>
  <div class="brand" style="top:130px;font-size:20px">Noorhall</div>
  <div class="radio" style="left:13px"><i class="on"></i>Child</div>
  <div class="radio" style="left:84px"><i></i>Imam User</div>
  <div class="radio" style="left:163px"><i></i>Admin user</div>
  <div class="field select" style="top:218px;left:13px;width:227px">Number Of Children</div>
  <div class="field" style="top:247px;left:13px;width:227px">Name</div>
  <div class="field" style="top:276px;left:13px;width:227px">Age</div>
  <div class="field select" style="top:304px;left:13px;width:227px">Gender</div>
  <div class="field select" style="top:332px;left:13px;width:227px">Quran Reading Level</div>
  <div class="btn" style="top:374px;left:13px;width:227px">Register</div>
</section>

<!-- Forget Password -->
<section class="screen forgot" style="left:815px;top:889px">
  <header class="header"><i class="back"></i><div class="header-title">Forget Password</div></header>
  <div class="heading" style="top:123px;left:20px">Forgot Your Password?</div>
  <div class="el" style="left:22px;top:150px;width:210px;font-size:6.5px;color:var(--muted);line-height:1.3">Forgot your password? entery your email address here to reset your password</div>
  <div class="field" style="top:184px;height:25px;color:var(--muted)">Your Email</div>
  <div class="btn" style="top:231px;width:94px;height:27px">Reset</div>
</section>

<!-- Make Donation -->
<section class="screen donation" style="left:127px;top:1599px">
  <header class="header"><i class="back"></i><div class="header-title">Make Donation</div></header>
  <div class="heading" style="top:101px">Select Amount</div>
  <div class="amount" style="left:13px;width:47px">$50</div>
  <div class="amount active" style="left:74px;width:45px">$100</div>
  <div class="amount" style="left:134px;width:46px">$500</div>
  <div class="amount" style="left:194px;width:46px">$1000</div>
  <div class="field" style="top:159px;left:13px;width:227px;height:24px;color:var(--muted)">$ &nbsp;Custom Amount</div>
  <div class="heading" style="top:208px">Select Purpose</div>
  <div class="field select" style="top:233px;left:13px;width:227px;height:25px;color:var(--muted)">List of Campains</div>
  <div class="heading" style="top:282px;left:12px">Payment Method</div>
  <div class="tab active" style="left:13px;width:112px">Credit Card</div>
  <div class="tab" style="left:129px;width:111px">Paylio</div>
  <div class="card-panel">
    <span style="left:11px;top:10px">Card Number</span><span style="left:119px;top:10px">Card Holder Name</span>
    <i style="left:11px;top:22px;width:104px"></i><i style="left:119px;top:22px;width:104px"></i>
    <span style="left:11px;top:47px">Expiry Date</span><span style="left:119px;top:47px">CVV</span>
    <i style="left:11px;top:59px;width:104px"></i><i style="left:119px;top:59px;width:104px"></i>
  </div>
  <div class="el" style="left:13px;top:445px;font-size:6px">Term and Conditions</div>
  <div class="el" style="left:13px;top:459px;font-size:6px;display:flex;align-items:center;gap:5px"><i style="width:8px;height:8px;border:1px solid #aaa;display:inline-block"></i>I agree to these Term and Conditions</div>
  <div class="btn" style="top:482px;left:13px;width:227px">Proceed</div>
</section>

<!-- Total Donated -->
<section class="screen total" style="left:471px;top:1599px">
  <header class="header"><i class="back"></i><div class="header-title">Total Donated</div></header>
  <div class="el" style="left:0;right:0;top:101px;text-align:center;font-family:Poppins,sans-serif;font-weight:600;font-size:31px;color:var(--green)">$58,248</div>
  <div class="el" style="left:0;right:0;top:143px;text-align:center;font-size:8px">Total Donation</div>
  <div class="heading" style="top:171px;left:12px">Donation History</div>
  <div class="el" style="right:13px;top:175px;font-size:5.5px">View All ›</div>
  <div class="donor" style="left:12px;top:194px"><div class="avatar" role="img" aria-label="Donor profile photo"></div><div class="donor-name">Donor Name</div><div class="donor-date">Jan 22, 2021</div><div class="donor-for">For New Holy Quran</div><div class="pill">$100</div></div>
  <div class="donor" style="left:12px;top:250px"><div class="avatar" role="img" aria-label="Donor profile photo"></div><div class="donor-name">Donor Name</div><div class="donor-date">Jan 22, 2021</div><div class="donor-for">For New Holy Quran</div><div class="pill">$100</div></div>
  <div class="donor" style="left:12px;top:305px"><div class="avatar" role="img" aria-label="Donor profile photo"></div><div class="donor-name">Donor Name</div><div class="donor-date">Jan 22, 2021</div><div class="donor-for">For New Holy Quran</div><div class="pill">$100</div></div>
  <div class="donor" style="left:12px;top:359px"><div class="avatar" role="img" aria-label="Donor profile photo"></div><div class="donor-name">Donor Name</div><div class="donor-date">Jan 22, 2021</div><div class="donor-for">For New Holy Quran</div><div class="pill">$100</div></div>
  <div class="donor" style="left:12px;top:413px"><div class="avatar" role="img" aria-label="Donor profile photo"></div><div class="donor-name">Donor Name</div><div class="donor-date">Jan 22, 2021</div><div class="donor-for">For New Holy Quran</div><div class="pill">$100</div></div>
</section>

<!-- Donated History -->
<section class="screen history" style="left:815px;top:1599px">
  <header class="header"><i class="back"></i><div class="header-title">Donated History</div></header>
  <div class="month" style="top:103px">January 2021</div>
  <div class="donor" style="left:13px;top:127px"><div class="avatar" role="img" aria-label="Donor profile photo"></div><div class="donor-name">Donor Name</div><div class="donor-date">Jan 22, 2021</div><div class="donor-for">For New Holy Quran</div><div class="pill">$100</div></div>
  <div class="donor" style="left:13px;top:183px"><div class="avatar" role="img" aria-label="Donor profile photo"></div><div class="donor-name">Donor Name</div><div class="donor-date">Jan 22, 2021</div><div class="donor-for">For New Holy Quran</div><div class="pill">$100</div></div>
  <div class="month" style="top:248px;left:12px">December 2020</div>
  <div class="donor" style="left:13px;top:273px"><div class="avatar" role="img" aria-label="Donor profile photo"></div><div class="donor-name">Donor Name</div><div class="donor-date">Jan 22, 2021</div><div class="donor-for">For New Holy Quran</div><div class="pill">$100</div></div>
  <div class="donor" style="left:13px;top:329px"><div class="avatar" role="img" aria-label="Donor profile photo"></div><div class="donor-name">Donor Name</div><div class="donor-date">Jan 22, 2021</div><div class="donor-for">For New Holy Quran</div><div class="pill">$100</div></div>
  <div class="month" style="top:396px;left:12px">November 2020</div>
  <div class="donor" style="left:13px;top:421px"><div class="avatar" role="img" aria-label="Donor profile photo"></div><div class="donor-name">Donor Name</div><div class="donor-date">Jan 22, 2021</div><div class="donor-for">For New Holy Quran</div><div class="pill">$100</div></div>
</section>

<!-- Prayer Times -->
<section class="screen prayers" style="left:311px;top:2309px">
  <header class="header"><i class="back"></i><div class="header-title">Prayer Times</div></header>
  <div class="date-bar" style="top:106px;left:12px;width:229px;height:33px">Friday January 22, 2021</div>
  <div class="prayer-row" style="top:141px"><span>Fajr</span><em>04:00</em></div>
  <div class="prayer-row" style="top:196px"><span>Duhr</span><em>14:00</em></div>
  <div class="prayer-row" style="top:251px"><span>Asar</span><em>04:00</em></div>
  <div class="prayer-row" style="top:306px"><span>Magrib</span><em>18:45</em></div>
  <div class="prayer-row" style="top:361px"><span>Isha</span><em>20:00</em></div>
</section>

<!-- Prayer Times – time picker -->
<section class="screen picker" style="left:655px;top:2309px">
  <header class="header"><i class="back"></i><div class="header-title">Prayer Times</div></header>
  <div class="overlay"></div>
  <div class="behind"></div>
  <div class="dialog">
    <div class="dialog-time">11:00<small>AM</small></div>
    <svg class="el" style="left:0;top:68px" width="191" height="175" viewBox="0 68 191 175" font-family="Roboto, sans-serif" font-size="11" fill="#444" text-anchor="middle">
      <line x1="95" y1="151" x2="64" y2="97" stroke="#d3efe2" stroke-width="1.5"/>
      <circle cx="64" cy="97" r="11" fill="#cfeee0"/>
      <text x="64" y="101" fill="#17a061">11</text>
      <text x="95" y="93">12</text><text x="126" y="101">1</text><text x="149" y="124">2</text>
      <text x="157" y="155">3</text><text x="149" y="186">4</text><text x="126" y="209">5</text>
      <text x="95" y="217">6</text><text x="64" y="209">7</text><text x="41" y="186">8</text>
      <text x="33" y="155">9</text><text x="41" y="124">10</text>
    </svg>
    <div class="done">Done</div>
  </div>
</section>

</body>
</html>
```